Photography Website

I want a website to promote my photography business. Needs to have a portfolio section, about me section, blog, client log in/ private gallery and a contact/quotation form.

Obviously the aim is to get enquiries and hence to lead people to the quotation or contact details. Also the aim is to showcase my photography to further drive enquiries.

Design and aesthetic appeal is crucial.

You can see my FB page here: http://www.example-social.com/pages/Tamsin-Oakridge-Photography/573920184610375

I do mainly weddings, engagements and family shoots.

I'm looking for a design that is custom and unique - something that does not look like a standard template! As a creative professional, I require a design which has 'character' - some ways I think this can be achieved is by choosing theme colours to base the website on, some consistent motifs, printed background/wall paper...? Whilst I am interested in an 'original' design, I would like to maintain a clear minimalist site layout.

In summary, my website must have a 'bold artistic identity'- whether this is achieved by a contemporary, rustic or classic design is open to suggestion. The homepage example which is attached to this brief may help you understand what I mean. (example_homepage.jpg) - this is only an example and it is not necessary for it to be exactly like this - as experienced web-designers I'm sure you will be able to build upon the example/idea.
Updates

Hi, I realize this project needs a bit more guidance so here goes....

I'm looking for a design that is custom and unique - something that does not look like a standard template! As a creative professional, I require a design which has 'character' - some ways I think this can be achieved is by choosing theme colours to base the website on, some consistent motifs, printed background/wall paper...?  Whilst I am interested in an 'original' design, I would like to maintain a clear minimalist site layout.

In summary, my website must have a 'bold artistic identity'- whether this is achieved by a contemporary, rustic or classic design is open to suggestion.

I hope this helps in giving you a better idea about what I am after....

Best,
Tamsin

Have just seen this - absolutely love it!  Similar designs please :)

www.lucyvantrell.example

Target Market(s)

Young families & young couples in the UK. Often professionals, large budget, trendy individuals.

Industry/Entity Type

Business

Requirements
Must have
• Portfolio section ( divided into: weddings, family, engagement, new born etc.)
about me section
A dedicated blog
client log in/ private gallery
contact/quotation form (easily found on web page)
'artistic identity' (see project overview above for more info)
Clean and clear layout
Based around my logo as attached
Nice to have
• I like soft pastel colours but open to suggestion
Whimsical/ retro/ 'quaint' feel to the design/fonts/color...again, open to all ideas...

www.lucyvantrell.example - this site is brilliant, with a simpler layout and less flash. I like the simple homepage especially.

```html
<!DOCTYPE html>
<html lang="en">
<head>
<meta charset="utf-8">
<title>Tamsin Oakridge Photography</title>
<link rel="stylesheet" href="https://fonts.googleapis.com/css2?family=Open+Sans:wght@400;600;700&display=swap">
<style>
:root{
  --backdrop:#eceef0;
  --page:#ffffff;
  --brand:#1a6fb5;
  --ink:#3a3a3a;
  --muted:#8a8a8a;
  --body-text:#6b5a55;
  --rule:#dcdcdc;
  --footer:#f6f6f6;
  --arrow:#d6d6d6;
}
*{box-sizing:border-box;margin:0;padding:0}
html,body{width:797px;height:1200px;overflow:hidden}
body{background:var(--backdrop);font-family:"Open Sans",Arial,sans-serif;color:var(--ink);position:relative}
.page{position:absolute;left:83px;top:0;width:634px;height:1166px;background:var(--page);border-top:4px solid var(--brand);box-shadow:0 0 6px rgba(0,0,0,.12)}
.abs{position:absolute}
.brand{left:0;width:634px;top:52px;text-align:center}
.brand-name{font-size:23px;font-weight:400;letter-spacing:2px;color:var(--brand);text-transform:uppercase;line-height:1.1}
.brand-sub{font-size:9.5px;letter-spacing:3px;color:var(--brand);text-transform:uppercase;margin-top:3px}
.site-nav{left:16px;top:110px;width:600px;display:flex;gap:20px}
.site-nav a{flex:1;font-size:7.5px;color:#444;text-decoration:none;border-top:1px solid var(--rule);padding-top:6px;text-transform:uppercase}
.site-nav a.current{border-top-color:#999}
.site-nav a.plain{border-top-color:transparent}
.hero{left:0;top:139px;width:634px;height:259px;background:linear-gradient(120deg,#d8d2cc 0%,#7a6f68 40%,#2c2826 55%,#b9b1aa 80%,#8c847e 100%)}
.welcome{left:0;width:634px;top:418px;text-align:center;font-size:15.5px;color:#6a6a6a}
.welcome b{color:#555;font-weight:700}
.shade{left:18px;width:598px;height:12px;border-radius:50%;box-shadow:0 6px 6px -4px rgba(0,0,0,.18)}
.section-title{font-size:12.5px;color:#333}
.work{width:184px}
.work .frame{width:184px;height:93px;border:1px solid #e4e4e4;padding:3px;background:#fff}
.work .frame div{width:100%;height:100%}
.work h3{font-size:10px;font-weight:400;color:#333;margin:12px 0 0 2px}
.work p{font-size:7.5px;color:#8a7f7b;line-height:1.6;margin:6px 0 0 2px}
.arrow{width:28px;height:42px;background:var(--arrow);top:538px}
.service-text{font-size:7.8px;color:var(--body-text);line-height:1.65;width:130px}
.service-list{list-style:none;font-size:7.5px;color:#777}
.service-list li{display:flex;align-items:center;gap:6px;height:16px}
.activity .thumb{width:95px;height:62px;border:1px solid #e4e4e4;padding:3px;background:#fff}
.activity .thumb div{width:100%;height:100%}
.activity h4{font-size:9.5px;font-weight:400;color:#333}
.activity p{font-size:7.5px;color:var(--body-text);line-height:1.75;width:325px;margin-top:8px}
.activity p b{color:#333;font-weight:600}
.footer{left:0;top:955px;width:634px;height:178px;background:var(--footer)}
.foot-col h5{font-size:10px;font-weight:400;color:#333;margin-bottom:10px}
.foot-col p{font-size:7.3px;color:var(--body-text);line-height:1.75}
.foot-col strong{font-weight:400;color:#333}
.subscribe{display:flex;gap:6px;margin-top:12px}
.subscribe span{display:block;width:136px;height:16px;border:1px solid #ddd;background:#fff;font-size:6.5px;color:#999;padding:3px 4px}
.subscribe em{display:block;font-style:normal;width:30px;height:16px;border:1px solid #ccc;background:#f2f2f2;font-size:6.5px;color:#555;text-align:center;padding-top:3px;border-radius:2px}
.email{color:var(--brand)}
.copyright{left:10px;top:1144px;font-size:7.3px;color:#aaa}
.copyright span{color:var(--brand)}
.foot-nav{right:14px;top:1142px;font-size:7.3px;color:#888}
</style>
</head>
<body>
<div class="arrow abs" style="left:55px">
  <svg width="28" height="42"><path d="M17 14 L11 21 L17 28" stroke="#fff" stroke-width="3" fill="none"/></svg>
</div>
<div class="arrow abs" style="left:717px">
  <svg width="28" height="42"><path d="M11 14 L17 21 L11 28" stroke="#fff" stroke-width="3" fill="none"/></svg>
</div>

<main class="page">
  <header class="brand abs">
    <div class="brand-name">Tamsin Oakridge</div>
    <div class="brand-sub">Photography</div>
  </header>

  <nav class="site-nav abs">
    <a class="current">Home</a><a>About Us</a><a>Portfolio</a><a>Blog</a><a>Contact</a><a class="plain">Login</a>
  </nav>

  <div class="hero abs" role="img" aria-label="Black and white photo of a young couple with their newborn baby beside a flower"></div>

  <p class="welcome abs">Welcome to <b>Tamsin Oakridge Photography</b>. We make white space look pretty.</p>
  <div class="shade abs" style="top:448px"></div>

  <h2 class="section-title abs" style="left:23px;top:484px">Recent Best Design</h2>
  <article class="work abs" style="left:23px;top:509px">
    <div class="frame"><div role="img" aria-label="Couple posing by a brick wall" style="background:linear-gradient(90deg,#6d6b68,#c9b8b6,#e0a9c0)"></div></div>
    <h3>Priya and Daniel</h3>
    <p>Lorem ipsum dolor sit amet, consectetuer adipiscing elit, sed diam nonummy.</p>
  </article>
  <article class="work abs" style="left:229px;top:509px">
    <div class="frame"><div role="img" aria-label="Mother and child at a photo day" style="background:linear-gradient(90deg,#f4f4f4,#3a2a28 35%,#f6f0ee 55%,#e985b4)"></div></div>
    <h3>Mums and Tots 2011</h3>
    <p>A few snaps from Mums and Tots 2011 photo day, back in May (I think)!</p>
  </article>
  <article class="work abs" style="left:435px;top:509px">
    <div class="frame"><div role="img" aria-label="Wedding couple seen beside a mirror" style="background:linear-gradient(90deg,#8a6a4a,#d8c8b4,#a2886c)"></div></div>
    <h3>Hana and Omar</h3>
    <p>I recently had the pleasure of photographing Hana and Omar's wedding.</p>
  </article>

  <div class="shade abs" style="top:680px"></div>

  <h2 class="section-title abs" style="left:18px;top:720px">Service News</h2>
  <p class="service-text abs" style="left:18px;top:752px">Lorem ipsum dolor sit amet, consectetur adipiscing elit. Ut vitae risus dolor. Duis vehicula fermentum eros ut tempor.</p>
  <ul class="service-list abs" style="left:18px;top:815px">
    <li><svg width="9" height="8"><path d="M1 4 L3.5 7 L8 1" stroke="#999" stroke-width="1.5" fill="none"/></svg>Wedding</li>
    <li><svg width="9" height="8"><path d="M1 4 L3.5 7 L8 1" stroke="#999" stroke-width="1.5" fill="none"/></svg>New born</li>
    <li><svg width="9" height="8"><path d="M1 4 L3.5 7 L8 1" stroke="#999" stroke-width="1.5" fill="none"/></svg>Maternity</li>
    <li><svg width="9" height="8"><path d="M1 4 L3.5 7 L8 1" stroke="#999" stroke-width="1.5" fill="none"/></svg>Family</li>
    <li><svg width="9" height="8"><path d="M1 4 L3.5 7 L8 1" stroke="#999" stroke-width="1.5" fill="none"/></svg>Event Photography</li>
  </ul>

  <h2 class="section-title abs" style="left:173px;top:720px">Recent Activity</h2>
  <div class="activity abs" style="left:173px;top:752px">
    <div class="thumb"><div role="img" aria-label="Guests at a gala dinner" style="background:linear-gradient(90deg,#6a4a40,#2a2220 50%,#8a6a5a)"></div></div>
  </div>
  <div class="activity abs" style="left:279px;top:752px">
    <h4>Lady Rosalind Trust Gala Dinner 2011</h4>
    <p>Etiam malesuada fringilla est a varius. Praesent quis dolor quis orci venenatis placerat. Maecenas facilisis. <b>Read more...</b></p>
  </div>
  <div class="activity abs" style="left:173px;top:834px">
    <div class="thumb"><div role="img" aria-label="Red tulip among green leaves" style="background:linear-gradient(90deg,#8fbf3a,#d8242a 50%,#6ea830)"></div></div>
  </div>
  <div class="activity abs" style="left:279px;top:834px">
    <h4>Summer and Autumn</h4>
    <p>Etiam malesuada fringilla est a varius. Praesent quis dolor quis orci venenatis placerat. Maecenas facilisis. <b>Read more...</b></p>
  </div>

  <footer class="footer abs">
    <div class="foot-col abs" style="left:18px;top:24px;width:190px">
      <h5>Keep Update With Us!</h5>
      <p>Our newsletter delivers to your inbox. Free receive updates, tips, support and inspiration once a month.</p>
      <div class="subscribe"><span>Enter your email address</span><em>Send</em></div>
    </div>
    <div class="foot-col abs" style="left:224px;top:24px;width:180px">
      <h5>Latest Post</h5>
      <p><strong>Integer eu nulla eu nisi vulputate varius</strong><br>Etiam malesuada fringilla est a varius. Praesent quis dolor quis orci venenatis placerat. Maecenas facilisis</p>
      <p style="margin-top:6px"><strong>Quisque consequat sagittis scelerisque</strong><br>Etiam malesuada fringilla est a varius. Praesent quis dolor quis orci venenatis placerat. Maecenas facilisis</p>
    </div>
    <div class="foot-col abs" style="left:430px;top:24px;width:190px">
      <h5>Street Address</h5>
      <p>12 Larkspur Lane, Millbrook<br>Birmingham, United Kingdom<br>Phone: +44 770 000 0123<br>Fax: +44 770 000 0123<br>Email: <span class="email">hello@tamsinoakridge.example</span></p>
    </div>
  </footer>

  <p class="copyright abs">Copyright © 2011 <span>Tamsin Oakridge Photography</span>. All Rights Reserved.</p>
  <p class="foot-nav abs">Home | About Us | Services | Blog | Portfolio | Contact</p>
</main>
</body>
</html>
```